Business Card Design for Norvane - The Asset Growth Company

We help people create wealth through real estate investments in the Greater Phoenix area. We buy, renovate, sell, and manage real estate. We handle everything from single family homes to apartment buildings, and some commercial projects including our fi

```html
<!DOCTYPE html>
<html lang="en">
<head>
<meta charset="utf-8">
<title>Norvane Business Card</title>
<link href="https://fonts.googleapis.com/css2?family=Oswald:wght@400;500&family=Cinzel:wght@500&display=swap" rel="stylesheet">
<style>
  :root {
    --backdrop: #1b1b1c;
    --card-dark: #111112;
    --card-light: #efefec;
    --gold: #c9a227;
    --ink: #4a4a4a;
    --ink-soft: #8a8a88;
    --rule: #d6d6d2;
  }
  * { margin: 0; padding: 0; box-sizing: border-box; }
  html, body { width: 1200px; height: 675px; overflow: hidden; }
  body {
    background: var(--backdrop);
    font-family: "Oswald", sans-serif;
    position: relative;
  }
  .card {
    position: absolute;
    top: 194px;
    width: 500px;
    height: 286px;
    border-radius: 3px;
  }
  .card-front {
    left: 75px;
    background: var(--card-dark);
    display: flex;
    flex-direction: column;
    align-items: center;
    justify-content: center;
  }
  .brand-mark {
    display: flex;
    align-items: center;
    gap: 12px;
  }
  .brand-square {
    width: 22px;
    height: 22px;
    background: var(--gold);
  }
  .brand-name {
    font-family: "Cinzel", serif;
    font-weight: 500;
    font-size: 44px;
    letter-spacing: 4px;
    color: var(--gold);
  }
  .front-web {
    margin-top: 26px;
    font-size: 11px;
    letter-spacing: 2px;
    color: var(--gold);
  }
  .badges {
    margin-top: 10px;
    display: flex;
    gap: 10px;
  }
  .badge {
    width: 16px;
    height: 16px;
    border: 1.5px solid var(--gold);
  }
  .card-back {
    left: 625px;
    background: var(--card-light);
    display: flex;
    align-items: center;
    padding: 0 30px;
  }
  .back-brand {
    width: 190px;
    display: flex;
    flex-direction: column;
    align-items: flex-start;
  }
  .back-brand .brand-name {
    font-size: 28px;
    letter-spacing: 3px;
    color: var(--ink);
  }
  .back-brand .brand-square { width: 14px; height: 14px; }
  .tagline {
    margin-top: 6px;
    font-size: 7.5px;
    letter-spacing: 1.6px;
    color: var(--ink-soft);
    text-transform: uppercase;
  }
  .divider {
    width: 1px;
    height: 150px;
    background: var(--rule);
    margin: 0 26px 0 4px;
  }
  .contact { flex: 1; }
  .person-name {
    font-size: 24px;
    font-weight: 500;
    letter-spacing: 1.5px;
    color: var(--gold);
    text-transform: uppercase;
  }
  .person-title {
    font-size: 10px;
    letter-spacing: 1.5px;
    color: var(--gold);
    text-transform: uppercase;
    margin-bottom: 14px;
  }
  .contact-line {
    font-size: 10px;
    letter-spacing: 1px;
    color: var(--ink);
    line-height: 1.9;
  }
  .contact-line .label { color: var(--gold); margin-right: 4px; }
</style>
</head>
<body>
  <section class="card card-front" aria-label="Card front">
    <div class="brand-mark">
      <span class="brand-square"></span>
      <span class="brand-name">NORVANE</span>
    </div>
    <p class="front-web">WWW.NORVANEREALTY.COM</p>
    <div class="badges">
      <span class="badge"></span>
      <span class="badge"></span>
      <span class="badge"></span>
    </div>
  </section>

  <section class="card card-back" aria-label="Card back">
    <div class="back-brand">
      <div class="brand-mark">
        <span class="brand-square"></span>
        <span class="brand-name">NORVANE</span>
      </div>
      <p class="tagline">The Asset Growth Company</p>
    </div>
    <div class="divider"></div>
    <div class="contact">
      <h1 class="person-name">Adrian Kessler</h1>
      <p class="person-title">Acquisition Associate</p>
      <p class="contact-line">adrian@norvanerealty.com</p>
      <p class="contact-line"><span class="label">O:</span>480 . 555 . 0142 &nbsp; <span class="label">C:</span>602 . 555 . 0187</p>
      <p class="contact-line">4120 E. Ridgeline Way &nbsp;|&nbsp; Suite 210</p>
      <p class="contact-line">Scottsdale, AZ 85250</p>
    </div>
  </section>
</body>
</html>
```